Copper Pathfinders (WordPress Hosting)

The site I would like is a robust message board. Each forum will be a group of people discussing and tracking their goals. I would also like areas
on the site for advertisers. Something similar to https://uprising.geargrowthhub.com/

Coding

Coded - Design and coding required

Number of Pages Required

1 page

Requirements
Must have
• Message Board

```html
<!DOCTYPE html>
<html lang="en">
<head>
<meta charset="utf-8">
<title>Copper Pathfinders — Forums</title>
<link rel="stylesheet" href="https://fonts.googleapis.com/css2?family=Lato:wght@400;700&family=Roboto:wght@400;500&display=swap">
<style>
:root{
  --orange:#ff4206;
  --orange-text:#f2420c;
  --green:#5f9e33;
  --green-light:#7ab32e;
  --tab-grey:#e6e6e6;
  --row-alt:#f3f3f3;
  --line:#d9d9d9;
  --ink:#2b2b2b;
  --white:#fff;
}
*{box-sizing:border-box;margin:0;padding:0}
html,body{width:1200px;height:2476px;overflow:hidden;background:var(--white)}
body{font-family:'Lato',sans-serif;color:var(--ink);position:relative}

.site-header{position:relative;height:241px}
.brand{position:absolute;left:110px;top:30px;display:flex;align-items:center;gap:12px}
.brand-mark{width:34px;height:34px;border-radius:50%;background:var(--green-light)}
.brand-name{font-family:'Lato',sans-serif;font-weight:700;font-size:26px;color:var(--green-light);line-height:1}
.account{position:absolute;right:113px;top:22px;display:flex;align-items:center;gap:30px}
.sign-in{color:var(--orange-text);font-size:16px;display:flex;align-items:center;gap:10px}
.sign-up{background:var(--orange);color:var(--white);font-size:16px;width:89px;height:34px;display:flex;align-items:center;justify-content:center}
.search{position:absolute;left:856px;top:87px;width:232px;height:45px;background:var(--orange);display:flex;align-items:center;padding:3px}
.search span{flex:1;color:var(--white);font-size:19px;padding-left:30px}
.search .btn{width:58px;height:39px;background:var(--white);display:flex;align-items:center;justify-content:center}

.main-nav{position:absolute;top:191px;left:0;height:50px;font-family:'Roboto',sans-serif}
.tab{position:absolute;top:0;height:50px;background:var(--tab-grey);color:var(--ink);font-size:18px;display:flex;align-items:center;justify-content:center}
.tab.active{background:var(--orange);color:var(--white)}
.sub-nav{position:absolute;top:241px;left:0;width:1200px;height:54px;background:var(--orange);font-family:'Roboto',sans-serif;color:var(--white);font-size:18px}
.sub-nav a{position:absolute;top:16px;color:var(--white);text-decoration:none}

.crumbs{position:absolute;top:350px;left:34px;right:46px;height:38px}
.home{position:absolute;left:0;top:0;display:flex;align-items:center;gap:16px;color:var(--orange-text);font-size:22px;font-weight:700}
.all-activity{position:absolute;right:0;top:0;display:flex;align-items:center;gap:14px;color:var(--orange-text);font-size:23px;font-weight:700}
.all-activity i{width:19px;height:19px;border-radius:50%;background:var(--green);display:block}

.panel{position:absolute;left:22px;width:1156px;border:1px solid var(--line);border-top:none}
.panel-head{height:56px;background:var(--green);color:var(--white);font-size:18px;font-weight:700;display:flex;align-items:center;padding-left:52px;position:relative;text-transform:uppercase}
.panel-head svg{position:absolute;right:30px;top:19px}
.browsing .body{height:78px;padding:28px 0 0 86px;font-size:18px;font-weight:700;color:#222}

.forums-bar{position:absolute;top:598px;left:24px;width:1155px;height:59px}
.forums-bar h2{position:absolute;left:0;top:14px;color:var(--orange-text);font-size:21px;font-weight:700}
.select-topic{position:absolute;right:0;top:0;width:274px;height:59px;background:var(--orange);color:var(--white);font-size:21px;font-weight:700;display:flex;align-items:center;justify-content:center}

.row{position:relative;height:126px;border-top:1px solid #e4e4e4}
.row.alt{background:var(--row-alt);height:100px}
.row .icon{position:absolute;left:53px;top:14px;width:57px;height:57px}
.row.alt .icon{top:12px}
.row .title{position:absolute;left:134px;top:27px;font-size:18px;font-weight:700;color:#333}
.row .desc{position:absolute;left:134px;top:60px;width:400px;font-size:15px;line-height:21px;color:var(--orange-text)}
.row .stats{position:absolute;left:676px;top:31px;width:120px;text-align:center;font-weight:700;color:#333}
.row .stats b{display:block;font-size:22px}
.row .stats span{display:block;font-size:17px;margin-top:10px}
.row .avatar{position:absolute;left:901px;top:31px;width:40px;height:40px;border-radius:50%}
.row .meta{position:absolute;left:953px;top:38px;font-size:15px;line-height:23px;color:#333}
.row .meta a{color:var(--orange-text);text-decoration:none;display:block}

.site-footer{position:absolute;left:0;top:2424px;width:1200px;height:52px;background:var(--orange);color:var(--white);font-size:13px}
.site-footer .copy{position:absolute;left:110px;top:18px}
.site-footer .code{position:absolute;right:62px;top:19px;font-size:11px}
</style>
</head>
<body>

<svg width="0" height="0" style="position:absolute">
  <defs>
    <symbol id="bubbles" viewBox="0 0 57 57">
      <path d="M31 16c-9 0-16 5.5-16 12.3 0 3.6 2 6.8 5.2 9l-2 6 7-3.6c1.8.5 3.7.7 5.8.7 9 0 16-5.5 16-12.3S40 16 31 16z" fill="none" stroke="#fff" stroke-width="3"/>
      <path d="M22 20c-5 1.6-8 5-8 9" fill="none" stroke="#fff" stroke-width="3"/>
    </symbol>
  </defs>
</svg>

<header class="site-header">
  <div class="brand"><span class="brand-mark"></span><span class="brand-name">Ironbound Vitality</span></div>
  <div class="account">
    <span class="sign-in">Existing user? Sign In
      <svg width="18" height="10" viewBox="0 0 18 10"><path d="M0 0h18L9 10z" fill="#f2420c"/></svg></span>
    <span class="sign-up">Sign Up</span>
  </div>
  <div class="search"><span>Search</span>
    <div class="btn"><svg width="22" height="22" viewBox="0 0 22 22"><circle cx="9" cy="9" r="7" fill="none" stroke="#222" stroke-width="3"/><path d="M14 14l6 6" stroke="#222" stroke-width="3.5" stroke-linecap="round"/></svg></div>
  </div>
  <nav class="main-nav">
    <span class="tab active" style="left:114px;width:155px">Ironbound Vitality</span>
    <span class="tab" style="left:281px;width:183px">Private Coaching</span>
    <span class="tab" style="left:473px;width:126px">Browse</span>
    <span class="tab" style="left:611px;width:179px">5 Week Challenge</span>
    <span class="tab" style="left:800px;width:130px">Activity</span>
    <span class="tab" style="left:940px;width:146px">Leaderboard</span>
  </nav>
</header>
<nav class="sub-nav"><a style="left:110px">Forums</a><a style="left:225px">Contact / Help</a></nav>

<div class="crumbs">
  <span class="home"><svg width="36" height="34" viewBox="0 0 36 34"><path d="M18 2L1 17l3 3 3-2.6V32h9v-9h4v9h9V17.4l3 2.6 3-3z" fill="#5f9e33"/></svg>Home</span>
  <span class="all-activity"><i></i>All Activity</span>
</div>

<section class="panel browsing" style="top:419px">
  <div class="panel-head">Recently Browsing&nbsp;&nbsp; 2 Members</div>
  <div class="body">Echoceanic&nbsp; Adrianne</div>
</section>

<div class="forums-bar"><h2>Forums</h2><span class="select-topic">Select Forum Topic</span></div>

<section class="panel" style="top:699px">
  <div class="panel-head">Welcome<svg width="24" height="16" viewBox="0 0 24 16"><path d="M2 3l10 10L22 3" fill="none" stroke="#fff" stroke-width="4"/></svg></div>
  <div class="row">
    <svg class="icon" viewBox="0 0 57 57"><path d="M31 16c-9 0-16 5.5-16 12.3 0 3.6 2 6.8 5.2 9l-2 6 7-3.6c1.8.5 3.7.7 5.8.7 9 0 16-5.5 16-12.3S40 16 31 16z" fill="#eee"/><path d="M22 20c-5 1.6-8 5-8 9" fill="none" stroke="#eee" stroke-width="3"/></svg>
    <div class="title">Lorem Ipsum</div><div class="desc">Lorem ipsum dolor sit amet, consectetur adipiscing elit,</div>
    <div class="stats"><b>6621</b><span>posts</span></div>
    <div class="avatar" role="img" aria-label="Member avatar photo" style="background:#6b4a34"></div>
    <div class="meta"><a>Lorem ipsum dolor sit</a>By SkyGirl<br>Saturday at 12:08 AM</div>
  </div>
  <div class="row alt">
    <svg class="icon"><circle cx="28.5" cy="28.5" r="28.5" fill="#ff4206"/><use href="#bubbles"/></svg>
    <div class="title">Lorem Ipsum</div><div class="desc">Lorem ipsum dolor sit amet, consectetur adipiscing elit,</div>
    <div class="stats"><b>6621</b><span>posts</span></div>
    <div class="avatar" role="img" aria-label="Member avatar photo" style="background:#b0785a"></div>
    <div class="meta" style="top:25px"><a>Lorem ipsum dolor sit</a>By SkyGirl<br>August 29</div>
  </div>
</section>

<section class="panel" style="top:1051px">
  <div class="panel-head">Uprising Headquarters<svg width="24" height="16" viewBox="0 0 24 16"><path d="M2 3l10 10L22 3" fill="none" stroke="#fff" stroke-width="4"/></svg></div>
  <div class="row">
    <svg class="icon"><circle cx="28.5" cy="28.5" r="28.5" fill="#ff4206"/><use href="#bubbles"/></svg>
    <div class="title">Lorem Ipsum</div><div class="desc">Lorem ipsum dolor sit amet, consectetur adipiscing elit, sed do eiusmod tempor incididunt,</div>
    <div class="stats"><b>6621</b><span>posts</span></div>
    <div class="meta"><a>Lorem ipsum dolor sit</a>By The Shadow<br>Tuesday at 10:49 PM</div>
  </div>
  <div class="row alt">
    <svg class="icon"><circle cx="28.5" cy="28.5" r="28.5" fill="#ff4206"/><use href="#bubbles"/></svg>
    <div class="title">Lorem Ipsum</div><div class="desc">Lorem ipsum dolor sit amet, consectetur adipiscing elit,</div>
    <div class="stats"><b>3584</b><span>posts</span></div>
    <div class="avatar" role="img" aria-label="Member avatar photo" style="background:#a8704e"></div>
    <div class="meta" style="top:25px"><a>Lorem ipsum dolor sit</a>By SkyGirl<br>56 minutes ago</div>
  </div>
  <div class="row" style="height:130px">
    <svg class="icon"><circle cx="28.5" cy="28.5" r="28.5" fill="#ff4206"/><use href="#bubbles"/></svg>
    <div class="title">Lorem Ipsum</div><div class="desc">Lorem ipsum dolor sit amet, consectetur adipiscing elit,</div>
    <div class="stats"><b>8465</b><span>posts</span></div>
    <div class="avatar" role="img" aria-label="Member avatar photo" style="background:#8d7a6a"></div>
    <div class="meta"><a>Lorem ipsum dolor sit</a>By Mad Hatter<br>6 hours ago</div>
  </div>
  <div class="row alt">
    <svg class="icon"><circle cx="28.5" cy="28.5" r="28.5" fill="#ff4206"/><use href="#bubbles"/></svg>
    <div class="title" style="top:15px">Lorem Ipsum</div><div class="desc" style="top:48px">Lorem ipsum dolor sit amet, consectetur adipiscing elit, sed do eiusmod tempor incididunt ut labore et dolore</div>
    <div class="stats" style="top:19px"><b>3548</b><span>posts</span></div>
    <div class="avatar" role="img" aria-label="Member avatar photo" style="background:#a06a48;top:17px"></div>
    <div class="meta" style="top:24px"><a>Lorem ipsum dolor sit</a>By SkyGirl<br>Saturday at 12:08 AM</div>
  </div>
  <div class="row" style="height:129px">
    <svg class="icon"><circle cx="28.5" cy="28.5" r="28.5" fill="#ff4206"/><use href="#bubbles"/></svg>
    <div class="title">Lorem Ipsum</div><div class="desc">Lorem ipsum dolor sit amet, consectetur adipiscing elit,</div>
    <div class="stats"><b>1588</b><span>posts</span></div>
    <div class="avatar" role="img" aria-label="Member avatar photo" style="background:#7a5a44"></div>
    <div class="meta"><a>Lorem ipsum dolor sit</a>By The Shadow<br>41 minutes ago</div>
  </div>
  <div class="row alt" style="height:97px">
    <svg class="icon"><circle cx="28.5" cy="28.5" r="28.5" fill="#ff4206"/><use href="#bubbles"/></svg>
    <div class="title" style="top:15px">Lorem Ipsum</div><div class="desc" style="top:48px">Lorem ipsum dolor sit amet, consectetur adipiscing elit,</div>
    <div class="stats" style="top:19px"><b>8712</b><span>posts</span></div>
    <div class="avatar" role="img" aria-label="Member avatar photo" style="background:#5e4030;top:17px"></div>
    <div class="meta" style="top:24px"><a>Lorem ipsum dolor sit</a>By SkyGirl<br>August 29</div>
  </div>
</section>

<section class="panel" style="top:1845px">
  <div class="panel-head">Fitness Specialities<svg width="24" height="16" viewBox="0 0 24 16"><path d="M2 3l10 10L22 3" fill="none" stroke="#fff" stroke-width="4"/></svg></div>
  <div class="row">
    <svg class="icon"><circle cx="28.5" cy="28.5" r="28.5" fill="#ff4206"/><use href="#bubbles"/></svg>
    <div class="title">Lorem Ipsum</div><div class="desc">Lorem ipsum dolor sit amet, consectetur adipiscing elit, sed do eiusmod tempor i</div>
    <div class="stats"><b>4895</b><span>posts</span></div>
    <div class="avatar" role="img" aria-label="Member avatar photo" style="background:#6d4636"></div>
    <div class="meta"><a>Lorem ipsum dolor sit</a>By SkyGirl<br>Saturday at 12:08 AM</div>
  </div>
  <div class="row alt">
    <svg class="icon"><circle cx="28.5" cy="28.5" r="28.5" fill="#ff4206"/><use href="#bubbles"/></svg>
    <div class="title" style="top:15px">Lorem Ipsum</div><div class="desc" style="top:48px">Lorem ipsum dolor sit amet, consectetur adipiscing elit,</div>
    <div class="stats" style="top:19px"><b>3546</b><span>posts</span></div>
    <div class="avatar" role="img" aria-label="Member avatar photo" style="background:#4a3a30;top:17px"></div>
    <div class="meta" style="top:24px"><a>Lorem ipsum dolor sit</a>By SkyGirl<br>August 29</div>
  </div>
</section>

<section class="panel" style="top:2193px">
  <div class="panel-head">Ironbound Vitality<svg width="24" height="16" viewBox="0 0 24 16"><path d="M2 3l10 10L22 3" fill="none" stroke="#fff" stroke-width="4"/></svg></div>
  <div class="row" style="height:142px">
    <svg class="icon"><circle cx="28.5" cy="28.5" r="28.5" fill="#ff4206"/><use href="#bubbles"/></svg>
    <div class="title">Lorem Ipsum</div><div class="desc">Lorem ipsum dolor sit amet, consectetur adipiscing elit, sed do eiusmod tempor incididunt ut labore et dolore magna aliqua.</div>
    <div class="stats"><b>5468</b><span>posts</span></div>
    <div class="avatar" role="img" aria-label="Member avatar photo" style="background:#7b5440"></div>
    <div class="meta"><a>Lorem ipsum dolor sit</a>By SkyGirl<br>Saturday at 12:08 AM</div>
  </div>
</section>

<footer class="site-footer"><span class="copy">2019 © Copyrights. All rights reserved</span><span class="code">C36</span></footer>

</body>
</html>
```